Book cover design for Water & Sanitation book

I would like to have a book cover designed (front and back) for a book I'm writing that has interviews with leading experts working in the field of water & sanitation globally.

Please use this board - https://in.corvelloboard.com/tamsinquorle/pins/ - as inspiration.

The title of the book is "Lanterns By Orchards" and will need to be visible on the cover page. The size of the book will be portrait and 8 inches x 11 inches.

```html
<!DOCTYPE html>
<html lang="en">
<head>
<meta charset="utf-8">
<title>Lanterns By Orchards — Book Cover</title>
<link rel="stylesheet" href="https://fonts.googleapis.com/css2?family=Playfair+Display:wght@900&family=Courier+Prime:wght@700&display=swap">
<style>
  :root {
    --page-bg: #eeeff1;
    --lagoon: #5fd8e4;
    --sea: #2f86dc;
    --ocean: #2a5fd4;
    --deep: #1a36a3;
    --abyss: #0f2277;
    --weed: #0b1a5c;
    --mug-light: #a6e8f4;
    --mug-mid: #5ec4e4;
    --whale: #9fb6d8;
    --ink-white: #ffffff;
    --cover-shadow: rgba(20, 30, 60, 0.25);
  }
  * { margin: 0; padding: 0; box-sizing: border-box; }
  html, body {
    width: 1200px;
    height: 720px;
    overflow: hidden;
    background: var(--page-bg);
  }
  .spread { position: relative; width: 1200px; height: 720px; }
  .cover {
    position: absolute;
    top: 90px;
    width: 393px;
    height: 540px;
    overflow: hidden;
    box-shadow: 0 10px 28px var(--cover-shadow);
  }
  .cover--back { left: 180px; }
  .cover--front { left: 627px; }
  .cover__art { position: absolute; inset: 0; width: 100%; height: 100%; }
  .art-spot { position: absolute; }
  .back-blurb {
    position: absolute;
    left: 20px;
    right: 20px;
    top: 250px;
    color: var(--ink-white);
    font-family: "Courier Prime", "Courier New", monospace;
    font-weight: 700;
    text-align: center;
  }
  .back-blurb__heading {
    font-family: "Playfair Display", Georgia, serif;
    font-weight: 900;
    font-size: 32px;
    letter-spacing: 0.5px;
    margin-bottom: 6px;
  }
  .back-blurb__text { font-size: 17px; line-height: 1.25; }
  .back-blurb__line { display: block; }
  .book-title {
    position: absolute;
    left: 38px;
    top: 30px;
    color: var(--ink-white);
    font-family: "Playfair Display", Georgia, serif;
    font-weight: 900;
    font-size: 54px;
    line-height: 1.02;
    letter-spacing: 1px;
  }
  .book-title__line { display: block; }
  .book-title__line--indent { padding-left: 28px; }
</style>
</head>
<body>
<main class="spread">

  <section class="cover cover--back" aria-label="Back cover">
    <svg class="cover__art" viewBox="0 0 393 540" preserveAspectRatio="none" role="img" aria-label="Painted underwater scene, light turquoise water fading into deep blue">
      <defs>
        <linearGradient id="backWater" x1="0" y1="0" x2="0" y2="1">
          <stop offset="0" stop-color="var(--lagoon)"/>
          <stop offset="0.35" stop-color="var(--sea)"/>
          <stop offset="0.75" stop-color="var(--ocean)"/>
          <stop offset="1" stop-color="var(--abyss)"/>
        </linearGradient>
      </defs>
      <rect width="393" height="540" fill="url(#backWater)"/>
    </svg>
    <svg class="art-spot" style="left:0;top:50px;width:190px;height:170px" viewBox="0 0 190 170" role="img" aria-label="Faint painted whale swimming near the surface">
      <defs>
        <radialGradient id="backWhaleTop"><stop offset="0" stop-color="var(--whale)" stop-opacity="0.45"/><stop offset="1" stop-color="var(--whale)" stop-opacity="0"/></radialGradient>
      </defs>
      <ellipse cx="95" cy="85" rx="95" ry="85" fill="url(#backWhaleTop)"/>
    </svg>
    <svg class="art-spot" style="left:180px;top:370px;width:200px;height:90px" viewBox="0 0 200 90" role="img" aria-label="Faint painted whale tail in deep water">
      <defs>
        <radialGradient id="backWhaleLow"><stop offset="0" stop-color="var(--whale)" stop-opacity="0.35"/><stop offset="1" stop-color="var(--whale)" stop-opacity="0"/></radialGradient>
      </defs>
      <ellipse cx="100" cy="45" rx="100" ry="45" fill="url(#backWhaleLow)"/>
    </svg>
    <svg class="art-spot" style="left:0;bottom:0;width:393px;height:90px" viewBox="0 0 393 90" preserveAspectRatio="none" role="img" aria-label="Dark painted seaweed along the sea floor">
      <defs>
        <linearGradient id="backWeed" x1="0" y1="0" x2="0" y2="1"><stop offset="0" stop-color="var(--weed)" stop-opacity="0"/><stop offset="1" stop-color="var(--weed)" stop-opacity="0.85"/></linearGradient>
      </defs>
      <rect width="393" height="90" fill="url(#backWeed)"/>
    </svg>
    <div class="back-blurb">
      <h2 class="back-blurb__heading">About the book</h2>
      <p class="back-blurb__text">
        <span class="back-blurb__line">I'm writing that has interviews</span>
        <span class="back-blurb__line">with leading experts</span>
        <span class="back-blurb__line">working in the field of</span>
        <span class="back-blurb__line">water &amp; sanitation globally.</span>
      </p>
    </div>
  </section>

  <section class="cover cover--front" aria-label="Front cover">
    <svg class="cover__art" viewBox="0 0 393 540" preserveAspectRatio="none" role="img" aria-label="Painted underwater scene, bright blue water deepening to navy">
      <defs>
        <linearGradient id="frontWater" x1="0" y1="0" x2="0" y2="1">
          <stop offset="0" stop-color="var(--ocean)"/>
          <stop offset="0.6" stop-color="var(--deep)"/>
          <stop offset="1" stop-color="var(--abyss)"/>
        </linearGradient>
      </defs>
      <rect width="393" height="540" fill="url(#frontWater)"/>
    </svg>
    <svg class="art-spot" style="left:180px;top:0;width:160px;height:70px" viewBox="0 0 160 70" role="img" aria-label="Faint painted whale near the surface">
      <defs>
        <radialGradient id="frontWhaleTop"><stop offset="0" stop-color="var(--whale)" stop-opacity="0.3"/><stop offset="1" stop-color="var(--whale)" stop-opacity="0"/></radialGradient>
      </defs>
      <ellipse cx="80" cy="35" rx="80" ry="35" fill="url(#frontWhaleTop)"/>
    </svg>
    <svg class="art-spot" style="left:140px;top:370px;width:170px;height:150px" viewBox="0 0 170 150" role="img" aria-label="Painted whale swimming upward among seaweed">
      <defs>
        <radialGradient id="frontWhaleLow"><stop offset="0" stop-color="var(--whale)" stop-opacity="0.5"/><stop offset="1" stop-color="var(--whale)" stop-opacity="0"/></radialGradient>
      </defs>
      <ellipse cx="85" cy="75" rx="85" ry="75" fill="url(#frontWhaleLow)"/>
    </svg>
    <svg class="art-spot" style="left:0;bottom:0;width:393px;height:170px" viewBox="0 0 393 170" preserveAspectRatio="none" role="img" aria-label="Dark painted seaweed rising from the sea floor">
      <defs>
        <linearGradient id="frontWeed" x1="0" y1="0" x2="0" y2="1"><stop offset="0" stop-color="var(--weed)" stop-opacity="0"/><stop offset="1" stop-color="var(--weed)" stop-opacity="0.9"/></linearGradient>
      </defs>
      <rect width="393" height="170" fill="url(#frontWeed)"/>
    </svg>
    <h1 class="book-title">
      <span class="book-title__line">Lanterns</span>
      <span class="book-title__line book-title__line--indent">By</span>
      <span class="book-title__line">Orchards</span>
    </h1>
    <svg class="art-spot" style="left:190px;top:215px;width:170px;height:140px" viewBox="0 0 170 140" role="img" aria-label="Drawn mug filled with light blue water">
      <defs>
        <radialGradient id="mugGlow" cx="0.45" cy="0.55" r="0.55">
          <stop offset="0" stop-color="var(--mug-light)" stop-opacity="0.95"/>
          <stop offset="0.6" stop-color="var(--mug-mid)" stop-opacity="0.7"/>
          <stop offset="1" stop-color="var(--mug-mid)" stop-opacity="0"/>
        </radialGradient>
      </defs>
      <ellipse cx="85" cy="70" rx="85" ry="70" fill="url(#mugGlow)"/>
    </svg>
  </section>

</main>
</body>
</html>
```